Veltora Software Business Card Design

We are a new organization called Veltora. We are a software as a service provider. We deliver a project and program management solution via the internet, so everyone has the ability to work together and collaborate. Its an enterprise platform and we will focus on 50 plus employee company.

We have a website in place
www.veltora-demo.com

Use this as a start of producing the business card. The logo is there as well, but if you have a great and better solution...

Color scheme's could be inline with the website, but don't pin point on it. We can always change the website, logo, color scheme etc.

Target Market(s)

B2B, Projectmembers, projectmanagers, ICT, CTO, Marketing Managers

Industry/Entity Type

Software

Requirements
Must have
• Marten Kuyvelsma

Tel: +31 255 47 09 36
Mob: +31 6 927 15 062
marten@veltora-demo.com
Oostelingpad 84c
2184 KT Nieuw Vennep

Www.veltora-demo.com
social media links

```html
<!DOCTYPE html>
<html lang="en">
<head>
<meta charset="utf-8">
<title>Veltora Business Card</title>
<link rel="stylesheet" href="https://fonts.googleapis.com/css2?family=Raleway:wght@300&family=Open+Sans:wght@400;600&display=swap">
<style>
  :root {
    --bg: #2f2f30;
    --card-white: #ffffff;
    --brand-green: #9ccc2c;
    --green-light: #b2db4a;
    --green-dark: #8cc12a;
    --ink: #1e1e1e;
    --ink-soft: #3a3a3a;
    --team-blue: #6fa6dc;
    --pm-orange: #e48f2e;
    --mgmt-green: #a8d23a;
    --photo-tone: #d9dcdf;
    --social-tone: #5a7fb0;
  }
  * { margin: 0; padding: 0; box-sizing: border-box; }
  html, body {
    width: 1200px; height: 700px; overflow: hidden;
    background: var(--bg);
    font-family: "Open Sans", Arial, sans-serif;
  }
  .stage { position: relative; width: 1200px; height: 700px; }
  .card {
    position: absolute; top: 200px;
    width: 520px; height: 300px;
    box-shadow: 0 10px 30px rgba(0,0,0,.45);
  }
  /* Front */
  .card-front { left: 60px; background: var(--card-white); color: var(--ink); }
  .brand-name {
    position: absolute; left: 34px; top: 26px;
    font-family: "Raleway", Arial, sans-serif; font-weight: 300;
    font-size: 58px; letter-spacing: 1px; color: var(--brand-green);
  }
  .person-name {
    position: absolute; left: 36px; top: 118px;
    font-size: 17px; font-weight: 400; color: var(--ink);
  }
  .contact-list { position: absolute; left: 36px; top: 146px; list-style: none; font-size: 12px; line-height: 17px; color: var(--ink-soft); }
  .contact-label { display: inline-block; width: 16px; color: var(--brand-green); font-weight: 600; }
  .address { position: absolute; left: 36px; top: 206px; font-size: 12px; color: var(--ink-soft); }
  .social-links { position: absolute; right: 34px; bottom: 26px; display: flex; gap: 5px; }
  .social-links span { width: 20px; height: 20px; border-radius: 3px; background: var(--social-tone); display: block; }
  /* Back */
  .card-back {
    left: 620px;
    background: radial-gradient(ellipse at 40% 40%, var(--green-light), var(--green-dark));
  }
  .role { position: absolute; display: flex; align-items: center; }
  .role-photo {
    width: 60px; height: 60px; border-radius: 50%;
    background: var(--photo-tone); border: 3px solid #fff;
  }
  .role-label {
    width: 62px; height: 62px; border-radius: 50%; margin-left: -12px;
    border: 3px solid #fff; display: flex; align-items: center; justify-content: center;
    text-align: center; color: #fff; font-size: 8px; font-weight: 600;
    letter-spacing: .5px; line-height: 11px; text-transform: uppercase;
  }
  .role-team { left: 70px; top: 70px; }
  .role-team .role-label { background: var(--team-blue); }
  .role-pm { left: 210px; top: 120px; }
  .role-pm .role-label { background: var(--pm-orange); }
  .role-mgmt { left: 360px; top: 170px; }
  .role-mgmt .role-label { background: var(--mgmt-green); }
  .website {
    position: absolute; left: 170px; top: 248px;
    font-size: 15px; font-weight: 600; color: #fff; letter-spacing: .5px;
  }
</style>
</head>
<body>
<main class="stage">
  <section class="card card-front">
    <div class="brand-name">Veltora</div>
    <div class="person-name">Marten Kuyvelsma</div>
    <ul class="contact-list">
      <li><span class="contact-label">m</span>+31 255 47 09 36</li>
      <li><span class="contact-label">p</span>+31 6 927 15 062</li>
      <li><span class="contact-label">e</span>marten@veltora-demo.com</li>
    </ul>
    <div class="address">Oostelingpad 84c, 2184 KT Nieuw Vennep</div>
    <div class="social-links" aria-label="Social media links">
      <span></span><span></span><span></span><span></span>
    </div>
  </section>

  <section class="card card-back">
    <div class="role role-team">
      <div class="role-photo" role="img" aria-label="Photo of a team member at work"></div>
      <div class="role-label">Team<br>Member</div>
    </div>
    <div class="role role-pm">
      <div class="role-photo" role="img" aria-label="Photo of a project manager in a suit"></div>
      <div class="role-label">Project<br>Manager</div>
    </div>
    <div class="role role-mgmt">
      <div class="role-photo" role="img" aria-label="Photo of a manager on the phone"></div>
      <div class="role-label">Management</div>
    </div>
    <div class="website">www.veltora-demo.com</div>
  </section>
</main>
</body>
</html>
```